Business Card Design for Engineering Firm

Need a business card design for small mechanical and plumbing engineering form based in Utah. Design should be customizable for all employees.

```html
<!DOCTYPE html>
<html lang="en">
<head>
<meta charset="UTF-8">
<title>Halverstone Engineering – Business Card</title>
<link href="https://fonts.googleapis.com/css2?family=Open+Sans:wght@400;600;700&display=swap" rel="stylesheet">
<style>
  :root {
    --page-bg: #3a3b3d;
    --brand-red: #7a0c10;
    --brand-red-dark: #3f0204;
    --brand-red-mid: #5e0508;
    --card-white: #ffffff;
    --card-grey: #ececec;
    --text-dark: #444444;
    --rule-grey: #9a9a9a;
  }
  * { box-sizing: border-box; margin: 0; padding: 0; }
  html, body {
    width: 1200px; height: 900px; overflow: hidden;
    background: var(--page-bg);
    font-family: "Open Sans", Arial, sans-serif;
  }
  .canvas { position: relative; width: 1200px; height: 900px; }

  .card {
    position: absolute;
    width: 600px; height: 343px;
    border-radius: 30px 0 30px 0;
    overflow: hidden;
    box-shadow: 0 14px 30px rgba(0,0,0,.45);
  }

  /* Front */
  .card-front {
    left: 90px; top: 70px;
    background: radial-gradient(ellipse at 35% 60%, var(--brand-red) 0%, var(--brand-red-mid) 50%, var(--brand-red-dark) 100%);
  }
  .front-brand {
    position: absolute; left: 0; right: 0; top: 148px;
    display: flex; align-items: center; justify-content: center; gap: 16px;
  }
  .brand-square { width: 30px; height: 30px; }
  .card-front .brand-square { background: #ffffff; }
  .brand-name {
    font-weight: 400; font-size: 26px; letter-spacing: 3px; text-transform: uppercase;
  }
  .card-front .brand-name { color: #ffffff; }

  /* Back */
  .card-back {
    left: 510px; top: 487px;
    background: linear-gradient(120deg, var(--card-grey) 0%, var(--card-white) 45%, var(--card-white) 100%);
  }
  .person { position: absolute; left: 40px; top: 32px; }
  .person-name { color: var(--brand-red); font-weight: 700; font-size: 17px; letter-spacing: .3px; }
  .person-role { color: var(--text-dark); font-size: 15px; margin-top: -2px; }

  .contact-list { position: absolute; left: 40px; top: 102px; list-style: none; }
  .contact-item {
    display: flex; align-items: center; gap: 10px;
    color: var(--text-dark); font-size: 14px; line-height: 25px;
  }
  .contact-icon { width: 15px; height: 15px; fill: none; stroke: var(--brand-red); stroke-width: 1.8; }

  .address {
    position: absolute; right: 36px; top: 88px; text-align: right;
    color: var(--text-dark); font-size: 14px; line-height: 20px;
  }

  .divider {
    position: absolute; left: 40px; right: 36px; top: 222px;
    border-top: 1px solid var(--rule-grey);
  }
  .back-brand {
    position: absolute; left: 0; right: 0; top: 256px;
    display: flex; align-items: center; justify-content: center; gap: 14px;
  }
  .card-back .brand-square { background: var(--brand-red); width: 26px; height: 26px; }
  .card-back .brand-name { color: var(--brand-red); font-size: 23px; }
</style>
</head>
<body>
<main class="canvas">

  <section class="card card-front" aria-label="Business card front">
    <div class="front-brand">
      <span class="brand-square"></span>
      <span class="brand-name">Halverstone Engineering</span>
    </div>
  </section>

  <section class="card card-back" aria-label="Business card back">
    <div class="person">
      <p class="person-name">MARK ELLISON</p>
      <p class="person-role">Director</p>
    </div>

    <ul class="contact-list">
      <li class="contact-item">
        <svg class="contact-icon" viewBox="0 0 16 16"><rect x="4" y="1" width="8" height="14" rx="1.5"/><line x1="7" y1="12.5" x2="9" y2="12.5"/></svg>
        300-555-0142
      </li>
      <li class="contact-item">
        <svg class="contact-icon" viewBox="0 0 16 16"><path d="M3 2l3 0 1 3-2 1.5a8 8 0 0 0 4.5 4.5L11 9l3 1v3a1.5 1.5 0 0 1-1.5 1.5A11 11 0 0 1 1.5 3.5 1.5 1.5 0 0 1 3 2z"/></svg>
        300-555-0142
      </li>
      <li class="contact-item">
        <svg class="contact-icon" viewBox="0 0 16 16"><rect x="1.5" y="3.5" width="13" height="9" rx="1"/><polyline points="1.5,4 8,9 14.5,4"/></svg>
        info@halverstoneengineering.com
      </li>
      <li class="contact-item">
        <svg class="contact-icon" viewBox="0 0 16 16"><circle cx="8" cy="8" r="6.5"/><ellipse cx="8" cy="8" rx="2.8" ry="6.5"/><line x1="1.5" y1="8" x2="14.5" y2="8"/></svg>
        www.halverstoneengineering.com
      </li>
    </ul>

    <address class="address" style="font-style:normal">
      42 Canyon Road<br>Provo, UT 84601
    </address>

    <div class="divider"></div>

    <div class="back-brand">
      <span class="brand-square"></span>
      <span class="brand-name">Halverstone Engineering</span>
    </div>
  </section>

</main>
</body>
</html>
```